Seafood Restaurant Outdoor Menu Board

Corvell's Seafood, a legendary local seafood restaurant in Ventura, CA USA, most widely known for its fish and chips and clam chowder, needs refreshed outdoor menu boards!

You can see the existing menu board at https://www.pictoshare.example/p/K8mR2Wxq51T/

and get inspiration from our website, https://corvellsseafood.example

Please use your design for 2 sets of menu items, to be displayed side by side as in the photo:
Menu Board #1: "Customer Favorites"
- Grilled Halibut
- Grilled Salmon Filet
- Grilled Shrimp Skewers
- Corvell's Fish & Chips
- 14pc Shrimp & Chips
- Harbor Trio
- Onion Rings
- Clam Chowder Lantern
- Large Clam Chowder
- Small Clam Chowder
Menu Board #2: "Grilled Dinners"
GR HALIBUT $21.80
BAKED HALIBUT $26.95
GR SNAPPER $21.95
GR AHI $25.85
GR SALMON FILLET $20.90
GR YELLOWTAIL $12.65
GR BLACK SEA BASS $20.99
GR SHRIMP SKEWERS $23.10
GR WHITE SEA BASS $21.60
GR SWORDFISH $27.75
GR MAHI $7.95
GR COD $10.40

SERVED WITH RICE PILAF & BREAD & YOUR CHOICE OF PASTA SALAD, COLE SLAW, OR GREEN SALAD

Our landlord has provided the following guidelines for the new menu board:
- Public Facing Exterior Menu boards need overall simplification and reduction of the information offered while still highlighting major sellers and up sellers.
- Need to be designed as elegant wall signs rather than a list of menu items. (see examples)
- Less is More.
- Easy to read and understand, equally spaced information, good use of negative space.
- Draw customers eyes to the most desirable products.
- Layout: The layout should be professionally done, with sufficient negative space around menu items.
- Fonts: 3 Fonts maximum, encouraging sans serif font styles for easy readability.
- Established 1982: Arial Rounded MT Bold
- Menu Boards: Myriad Pro - Bold Condensed
- Smaller Directional Signs: Arial
- Colors: Tied to organization branding, 3 colors maximum. Please use a light-colored background. Our brand colors are:
- Primary: #233F94
- Secondary: #0F65A7
- Tertiary: 32A0CA
- Contrast: #F7F4DB
Attention: #ED4224
Icons: Use of simplified icons are allowed and encouraged to highlight and organize menu sections

```html
<!DOCTYPE html>
<html lang="en">
<head>
<meta charset="utf-8">
<title>Corvell's Seafood – Menu Boards</title>
<link href="https://fonts.googleapis.com/css2?family=Figtree:wght@700;800&display=swap" rel="stylesheet">
<style>
  :root {
    --primary: #233F94;
    --contrast: #F7F4DB;
    --attention: #ED4224;
    --wall: #A9A9A9;
    --wave-tint: #D9DAD6;
  }
  * { box-sizing: border-box; margin: 0; padding: 0; }
  html, body { width: 1200px; height: 1036px; overflow: hidden; }
  body {
    background: var(--wall);
    font-family: "Figtree", "Helvetica Neue", Arial, sans-serif;
    color: var(--primary);
    position: relative;
  }
  .board {
    position: absolute;
    top: 72px;
    width: 524px;
    height: 891px;
    background: var(--primary);
    padding: 22px;
    box-shadow: 6px 8px 14px rgba(0,0,0,0.28);
  }
  .board--favorites { left: 58px; }
  .board--grilled { left: 618px; }
  .board__inner {
    position: relative;
    width: 100%;
    height: 100%;
    background: var(--contrast);
  }
  .content {
    position: absolute;
    left: 73px;
    width: 334px;
  }
  .brand {
    top: 62px;
    height: 82px;
    text-align: center;
    display: flex;
    align-items: center;
    justify-content: center;
    gap: 10px;
    font-size: 36px;
    font-weight: 800;
    letter-spacing: -0.5px;
    line-height: 1;
  }
  .brand__dot {
    width: 14px; height: 14px; border-radius: 50%;
    background: var(--primary);
  }
  .section-title {
    height: 60px;
    border-top: 2px solid var(--primary);
    border-bottom: 2px solid var(--primary);
    display: flex;
    align-items: center;
    justify-content: space-between;
    padding: 0 7px;
  }
  .section-title h2 {
    font-size: 22.5px;
    font-weight: 800;
    letter-spacing: 0.1px;
  }
  .section-title__mark {
    display: block;
    width: 22px;
    height: 8px;
    border-radius: 4px;
    background: var(--attention);
    opacity: 0.85;
  }
  .board--favorites .section-title { top: 196px; }
  .board--grilled .section-title { top: 48px; }
  .menu-list { list-style: none; }
  .board--favorites .menu-list { top: 297px; }
  .board--grilled .menu-list { top: 148px; }
  .menu-item {
    height: 35.6px;
    display: flex;
    align-items: center;
    font-size: 15.5px;
    font-weight: 800;
    letter-spacing: 0.2px;
  }
  .menu-item__name { white-space: nowrap; }
  .menu-item__leader {
    flex: 1;
    margin: 4px 16px 0 14px;
    border-bottom: 1.5px dotted var(--primary);
    opacity: 0.7;
  }
  .menu-item__price { width: 49px; white-space: nowrap; }
  .menu-item__price sup {
    font-size: 9.5px;
    vertical-align: 5px;
    margin-left: 1px;
  }
  .sides-note {
    top: 597px;
    height: 93px;
    background: var(--attention);
    color: var(--contrast);
    text-align: center;
    font-size: 12.3px;
    font-weight: 700;
    line-height: 17px;
    padding-top: 15px;
  }
  .sides-note__edge {
    position: absolute;
    left: 0; bottom: -1px;
    width: 334px; height: 10px;
  }
  .waves {
    height: 111px;
    background: linear-gradient(180deg, var(--wave-tint), #CFD2D8);
  }
  .board--favorites .waves { top: 693px; }
  .board--grilled .waves { top: 714px; height: 89px; }
</style>
</head>
<body>

<section class="board board--favorites">
  <div class="board__inner">
    <div class="content brand">
      <span class="brand__dot"></span>
      <span class="brand__name">Corvell's Seafood</span>
    </div>

    <header class="content section-title">
      <span class="section-title__mark" role="img" aria-label="Small fish icon"></span>
      <h2>CUSTOMER FAVORITES</h2>
      <span class="section-title__mark" role="img" aria-label="Small fish icon"></span>
    </header>

    <ul class="content menu-list">
      <li class="menu-item"><span class="menu-item__name">GRILLED HALIBUT</span><span class="menu-item__leader"></span><span class="menu-item__price">$30.<sup>99</sup></span></li>
      <li class="menu-item"><span class="menu-item__name">GRILLED SALMON FILET</span><span class="menu-item__leader"></span><span class="menu-item__price">$31.<sup>50</sup></span></li>
      <li class="menu-item"><span class="menu-item__name">GRILLED SHRIMP SKEWERS</span><span class="menu-item__leader"></span><span class="menu-item__price">$27.<sup>50</sup></span></li>
      <li class="menu-item"><span class="menu-item__name">CORVELL'S FISH &amp; CHIPS</span><span class="menu-item__leader"></span><span class="menu-item__price">$21.<sup>80</sup></span></li>
      <li class="menu-item"><span class="menu-item__name">14PC SHRIMP &amp; CHIPS</span><span class="menu-item__leader"></span><span class="menu-item__price">$25.<sup>85</sup></span></li>
      <li class="menu-item"><span class="menu-item__name">HARBOR TRIO</span><span class="menu-item__leader"></span><span class="menu-item__price">$27.<sup>75</sup></span></li>
      <li class="menu-item"><span class="menu-item__name">ONION RINGS</span><span class="menu-item__leader"></span><span class="menu-item__price">$9.<sup>05</sup></span></li>
      <li class="menu-item"><span class="menu-item__name">CLAM CHOWDER LANTERN</span><span class="menu-item__leader"></span><span class="menu-item__price">$14.<sup>85</sup></span></li>
      <li class="menu-item"><span class="menu-item__name">LARGE CLAM CHOWDER</span><span class="menu-item__leader"></span><span class="menu-item__price">$9.<sup>89</sup></span></li>
      <li class="menu-item"><span class="menu-item__name">SMALL CLAM CHOWDER</span><span class="menu-item__leader"></span><span class="menu-item__price">$6.<sup>59</sup></span></li>
    </ul>

    <div class="content waves" role="img" aria-label="Decorative wave pattern"></div>
  </div>
</section>

<section class="board board--grilled">
  <div class="board__inner">
    <header class="content section-title">
      <span class="section-title__mark" role="img" aria-label="Small fish icon"></span>
      <h2>GRILLED DINNERS</h2>
      <span class="section-title__mark" role="img" aria-label="Small fish icon"></span>
    </header>

    <ul class="content menu-list">
      <li class="menu-item"><span class="menu-item__name">GR HALIBUT</span><span class="menu-item__leader"></span><span class="menu-item__price">$21.<sup>80</sup></span></li>
      <li class="menu-item"><span class="menu-item__name">BAKED HALIBUT</span><span class="menu-item__leader"></span><span class="menu-item__price">$26.<sup>95</sup></span></li>
      <li class="menu-item"><span class="menu-item__name">GR SNAPPER</span><span class="menu-item__leader"></span><span class="menu-item__price">$21.<sup>95</sup></span></li>
      <li class="menu-item"><span class="menu-item__name">GR AHI</span><span class="menu-item__leader"></span><span class="menu-item__price">$25.<sup>85</sup></span></li>
      <li class="menu-item"><span class="menu-item__name">GR SALMON FILLET</span><span class="menu-item__leader"></span><span class="menu-item__price">$20.<sup>90</sup></span></li>
      <li class="menu-item"><span class="menu-item__name">GR YELLOWTAIL</span><span class="menu-item__leader"></span><span class="menu-item__price">$12.<sup>65</sup></span></li>
      <li class="menu-item"><span class="menu-item__name">GR BLACK SEA BASS</span><span class="menu-item__leader"></span><span class="menu-item__price">$20.<sup>99</sup></span></li>
      <li class="menu-item"><span class="menu-item__name">GR SHRIMP SKEWERS</span><span class="menu-item__leader"></span><span class="menu-item__price">$23.<sup>10</sup></span></li>
      <li class="menu-item"><span class="menu-item__name">GR WHITE SEA BASS</span><span class="menu-item__leader"></span><span class="menu-item__price">$21.<sup>60</sup></span></li>
      <li class="menu-item"><span class="menu-item__name">GR SWORDFISH</span><span class="menu-item__leader"></span><span class="menu-item__price">$27.<sup>75</sup></span></li>
      <li class="menu-item"><span class="menu-item__name">GR MAHI</span><span class="menu-item__leader"></span><span class="menu-item__price">$7.<sup>95</sup></span></li>
      <li class="menu-item"><span class="menu-item__name">GR COD</span><span class="menu-item__leader"></span><span class="menu-item__price">$10.<sup>40</sup></span></li>
    </ul>

    <div class="content sides-note">
      SERVED WITH RICE PILAF &amp; BREAD &amp;<br>
      YOUR CHOICE OF PASTA SALAD, COLE SLAW,<br>
      OR GREEN SALAD
      <svg class="sides-note__edge" viewBox="0 0 334 10" preserveAspectRatio="none" aria-hidden="true">
        <path d="M0 10 L0 3 Q10 10 21 7 Q32 0 42 5 Q52 10 63 7 Q74 0 84 5 Q94 10 105 7 Q116 0 126 5 Q136 10 147 7 Q158 0 168 5 Q178 10 189 7 Q200 0 210 5 Q220 10 231 7 Q242 0 252 5 Q262 10 273 7 Q284 0 294 5 Q304 10 315 7 Q326 0 334 4 L334 10 Z" fill="#F7F4DB"/>
      </svg>
    </div>

    <div class="content waves" role="img" aria-label="Decorative wave pattern"></div>
  </div>
</section>

</body>
</html>
```